Business Card Design Project

Small privately owned salon.

Industry/Entity Type

Business

Contact Information for Business Card

Hair salon.i would like my logo to be my name , Marisol Denby. Address and phone can go on the front or back. The back will be where I write their appt.
address-362 Thistledown lane York, Pa. 17488
Phone- 717-555-0148

```html
<!DOCTYPE html>
<html lang="en">
<head>
<meta charset="utf-8">
<title>Marisol Denby Hair Salon – Business Card</title>
<link href="https://fonts.googleapis.com/css2?family=Open+Sans:wght@400&display=swap" rel="stylesheet">
<style>
  :root {
    --ink: #2b2a29;
    --paper: #ffffff;
    --stage: #ffffff;
    --rule: #3a3938;
    --shadow: rgba(0,0,0,0.14);
  }
  * { margin: 0; padding: 0; box-sizing: border-box; }
  html, body {
    width: 1050px; height: 1200px; overflow: hidden;
    background: var(--stage);
    font-family: "Open Sans", Arial, sans-serif;
    color: var(--ink);
  }
  .canvas { position: relative; width: 1050px; height: 1200px; }

  .card {
    position: absolute; left: 182px; width: 669px; height: 412px;
    background: var(--paper);
    box-shadow: -6px 8px 14px var(--shadow);
    overflow: hidden;
  }
  .card--front { top: 164px; }
  .card--back  { top: 650px; }

  .band { position: absolute; left: 0; width: 100%; background: var(--ink); }
  .rule { position: absolute; left: 0; width: 100%; height: 6px; background: var(--ink); }

  .mark-square {
    position: absolute; background: var(--paper);
    border: 4px solid var(--ink);
    outline: 5px solid var(--paper);
  }

  /* front */
  .card--front .band { top: 0; height: 121px; }
  .card--front .rule { top: 125px; }
  .card--front .mark-square { left: 272px; top: 77px; width: 122px; height: 120px; }

  .brand {
    position: absolute; left: 0; width: 100%; top: 224px; text-align: center;
  }
  .brand__name {
    font-size: 34px; font-weight: 400; letter-spacing: 1px; color: var(--ink);
  }
  .brand__divider {
    width: 246px; margin: 8px auto 0; border-top: 1px dashed var(--ink);
  }
  .brand__tag {
    margin-top: 8px; font-size: 17px; letter-spacing: 5px; color: var(--ink);
  }

  /* back */
  .appointment { position: absolute; left: 138px; top: 56px; font-size: 19px; }
  .appointment__title { height: 63px; }
  .appointment__field { display: flex; align-items: flex-end; height: 63px; }
  .appointment__line {
    display: inline-block; border-bottom: 1px solid var(--ink);
    margin-left: 6px; height: 22px;
  }
  .appointment__field--date .appointment__line { width: 335px; }
  .appointment__field--time .appointment__line { width: 335px; }

  .card--back .rule { top: 281px; }
  .card--back .band { top: 292px; height: 120px; }
  .card--back .mark-square { left: 290px; top: 253px; width: 84px; height: 86px; }

  .contact {
    position: absolute; top: 362px; left: 58px;
    display: flex; align-items: center; color: var(--paper); font-size: 19px;
  }
  .contact__item { display: flex; align-items: center; gap: 10px; }
  .contact__item + .contact__item { margin-left: 26px; }
  .contact svg { fill: var(--paper); }
</style>
</head>
<body>
<main class="canvas">

  <section class="card card--front" aria-label="Card front">
    <div class="band"></div>
    <div class="rule"></div>
    <div class="mark-square" aria-hidden="true"></div>
    <div class="brand">
      <div class="brand__name">Marisol Denby</div>
      <div class="brand__divider"></div>
      <div class="brand__tag">HAIR SALON</div>
    </div>
  </section>

  <section class="card card--back" aria-label="Card back">
    <div class="appointment">
      <div class="appointment__title">Next appointment:</div>
      <div class="appointment__field appointment__field--date">Date<span class="appointment__line"></span></div>
      <div class="appointment__field appointment__field--time">Time<span class="appointment__line"></span></div>
    </div>
    <div class="rule"></div>
    <div class="band"></div>
    <div class="mark-square" aria-hidden="true"></div>
    <div class="contact">
      <div class="contact__item">
        <svg width="16" height="24" viewBox="0 0 16 24" aria-hidden="true">
          <path d="M8 0C3.6 0 0 3.5 0 7.9 0 13.5 8 24 8 24s8-10.5 8-16.1C16 3.5 12.4 0 8 0zm0 11a3 3 0 1 1 0-6 3 3 0 0 1 0 6z"/>
        </svg>
        <span>362 Thistledown lane York, Pa. 17488</span>
      </div>
      <div class="contact__item">
        <svg width="16" height="20" viewBox="0 0 16 20" aria-hidden="true">
          <path d="M4.2 0.5 6.6 4.6c.3.5.1 1.1-.3 1.4L4.7 7c.9 2.6 2.4 4.9 4.4 6.7l1.5-1.1c.5-.3 1.1-.2 1.4.2l2.8 3.8c.3.4.2 1-.2 1.4l-1.6 1.3c-1 .8-2.4.8-3.4.1C5 16.3 1.6 11.3.5 5.8.3 4.6.8 3.4 1.8 2.7L3.2.3c.3-.2.8-.1 1 .2z"/>
        </svg>
        <span>717-555-0148</span>
      </div>
    </div>
  </section>

</main>
</body>
</html>
```